Landing Page

basically our company has as an strategy to sell our subscription product a set os pages normally in 4 steps
1 - We show that the "customer" will win a prizze
2 - We show some advantages that we have as a company
3 - We show another prizze
4 - We explain that to gain all itens they should make a subscription with a HUGE discount
What do we need?
1 - a new proposal for our set of landing pages
2 - responsive layout for all pages
3 - ideas that can increase our conversion rates
Examples:
http://www.saibatudoagora.com/
http://www.saibatudoagora.com/camfly/index.php
http://www.saibatudoagora.com/pixelcart/index.php
http://www.saibatudoagora.com/v2/index.php
http://servicoglobal.guardiaq.org.br/index.aspx?prm_id_c=PZM13001
http://www.brindelar.com.br/br_rdb_pro_vsi_int_1.asp?mktcode=RDPN50
https://www.linkaro77.info/seq2012/twosteps/pt_br/b2013/index.html?lang=brpt_br&project=TwoSteps&codeprom=ECAD0901&tmpl=b2013&cn=EE00AE90-96EA-4C4D-9AC0-6E9CB5476B41#1
https://servicoglobal.guardiaq.org.br/step_03.aspx
It Company

```html
<!DOCTYPE html>
<html lang="en">
<head>
<meta charset="utf-8">
<title>Guardiaq – Subscribe to win a prize</title>
<link href="https://fonts.googleapis.com/css2?family=Ubuntu:wght@300;400;500&family=Lato:wght@400&display=swap" rel="stylesheet">
<style>
  :root{
    --page-bg:#ececec;
    --topbar:#272f33;
    --nav-text:#e6e9ea;
    --social:#8a8f92;
    --brand-red-top:#d63a22;
    --brand-red-bottom:#a2180c;
    --hero-light:#f1f1f2;
    --hero-mid:#d8d6d8;
    --form-frame:#8a8a8a;
    --title-red:#d8373a;
    --label:#666;
    --input-border:#c9c9c9;
    --muted:#8a8a8a;
    --btn-top:#8fd24f;
    --btn-bottom:#5b9e17;
    --btn-edge:#4b8a12;
    --heading:#4f4f4f;
    --feature-title:#6e6e6e;
    --icon-bg:#f0f0f0;
    --icon:#8e8e8e;
    --white:#fff;
  }
  *{box-sizing:border-box;margin:0;padding:0}
  html,body{width:1200px;height:1100px;overflow:hidden}
  body{position:relative;background:var(--page-bg);font-family:"Ubuntu",sans-serif;color:var(--muted)}
  .topbar{position:absolute;left:0;top:0;width:1200px;height:46px;background:var(--topbar)}
  .main-nav{position:absolute;left:111px;top:14px;font-family:"Lato",sans-serif;font-size:14px;color:var(--nav-text);display:flex}
  .main-nav a{color:inherit;text-decoration:none}
  .main-nav .sep{margin:0 11px;opacity:.8}
  .social{position:absolute;left:981px;top:10px;display:flex;gap:4px}
  .social span{width:24px;height:24px;border-radius:50%;background:var(--social);display:block}
  .brand-band{position:absolute;left:110px;top:46px;width:980px;height:102px;
    background:linear-gradient(var(--brand-red-top) 0%,#c52d18 45%,#b3200f 46%,var(--brand-red-bottom) 100%);}
  .brand-name{position:absolute;left:0;width:100%;top:22px;text-align:center;color:var(--white);
    font-family:"Ubuntu",sans-serif;font-weight:500;font-size:46px;letter-spacing:1px;line-height:60px}
  .hero{position:absolute;left:110px;top:148px;width:980px;height:568px;
    background:radial-gradient(ellipse at 25% 50%,#e9dcd6 0%,var(--hero-light) 40%,var(--hero-mid) 100%)}
  .signup{position:absolute;left:641px;top:241px;width:430px;height:380px;border:10px solid var(--form-frame);background:var(--white)}
  .signup h2{position:absolute;left:21px;top:18px;font-weight:400;font-size:30px;color:var(--title-red);white-space:nowrap}
  .field{position:absolute;left:0;width:400px;height:37px}
  .field label{position:absolute;right:307px;top:10px;font-size:14px;color:var(--label);white-space:nowrap}
  .field input{position:absolute;left:103px;top:0;width:285px;height:37px;border:1px solid var(--input-border);background:var(--white)}
  .signup .note{position:absolute;left:22px;top:256px;width:365px;font-size:13.5px;line-height:18px;color:var(--muted)}
  .signup button{position:absolute;left:20px;top:298px;width:370px;height:44px;border:1px solid var(--btn-edge);border-radius:3px;
    background:linear-gradient(var(--btn-top) 0%,#7bc33a 48%,#67ad21 52%,var(--btn-bottom) 100%);
    color:var(--white);font-family:"Ubuntu",sans-serif;font-size:20px;font-weight:400;text-transform:uppercase}
  .content{position:absolute;left:110px;top:716px;width:980px;height:325px;background:var(--white)}
  .content h1{position:absolute;left:16px;top:14px;font-weight:300;font-size:34px;color:var(--heading);white-space:nowrap}
  .content .intro{position:absolute;left:17px;top:64px;width:940px;font-size:14px;line-height:18px;color:var(--muted)}
  .feature{position:absolute;width:330px;height:62px}
  .feature .icon{position:absolute;left:5px;top:0;width:60px;height:60px;border-radius:50%;background:var(--icon-bg);display:flex;align-items:center;justify-content:center}
  .feature h3{position:absolute;left:84px;top:0;font-weight:400;font-size:16.5px;color:var(--feature-title);white-space:nowrap}
  .feature p{position:absolute;left:84px;top:24px;width:220px;font-size:13.5px;line-height:17px;color:var(--muted)}
  .footer{position:absolute;left:0;top:1062px;width:1200px;text-align:center;font-family:"Lato",sans-serif;font-size:13.5px;color:var(--muted)}
</style>
</head>
<body>
  <header class="topbar">
    <nav class="main-nav">
      <a href="#">About Us</a><span class="sep">I</span>
      <a href="#">What We Offer</a><span class="sep">I</span>
      <a href="#">Join</a><span class="sep">I</span>
      <a href="#">Contact</a><span class="sep">I</span>
      <a href="#">Press</a>
    </nav>
    <div class="social" aria-label="Social links"><span></span><span></span><span></span><span></span></div>
  </header>

  <div class="brand-band"><div class="brand-name">GUARDIAQ</div></div>

  <section class="hero" role="img" aria-label="Photo of a smiling woman holding a white gift box with a red ribbon on a soft light bokeh background"></section>

  <form class="signup">
    <h2>Get Subcribe to win a Prize</h2>
    <div class="field" style="top:59px"><label>Name:</label><input type="text"></div>
    <div class="field" style="top:105px"><label>Last Name:</label><input type="text"></div>
    <div class="field" style="top:151px"><label>Phone:</label><input type="text"></div>
    <div class="field" style="top:197px"><label>Email:</label><input type="text"></div>
    <p class="note">Lorem ipsum dolor sit amet consectetur adipsicing elit, Sed do euismod tempor incidunt magna aliqua...</p>
    <button type="button">Subcribe here to win a prize</button>
  </form>

  <main class="content">
    <h1>Basically our company has as an strategy to sell our subscription</h1>
    <p class="intro">Lorem ipsum dolor sit amet, consectetur adipisicing elit, sed do eiusmod tempor incididunt ut labore et dolore magna aliqua. Ut enim ad minim veniam, quis nostrud exercitation ullamco laboris nisi ut aliquip ex ea commodo consequat.</p>

    <div class="feature" style="left:0;top:133px">
      <div class="icon"><svg width="34" height="34" viewBox="0 0 34 34"><path d="M4 4h13l13 13-13 13L4 17z" fill="#8e8e8e" transform="rotate(10 17 17)"/><circle cx="10" cy="10" r="2.5" fill="#f0f0f0"/><text x="17" y="23" font-size="12" font-family="Ubuntu,sans-serif" fill="#f0f0f0" text-anchor="middle">$</text></svg></div>
      <h3>Customer will win a prizze</h3>
      <p>Lorem Ipsum is simply dummy text of the printing and typesetting</p>
    </div>
    <div class="feature" style="left:320px;top:133px">
      <div class="icon"><svg width="36" height="36" viewBox="0 0 36 36"><g fill="#8e8e8e" transform="translate(18 18)"><circle r="11"/><rect x="-3.5" y="-16" width="7" height="32" rx="1"/><rect x="-3.5" y="-16" width="7" height="32" rx="1" transform="rotate(45)"/><rect x="-3.5" y="-16" width="7" height="32" rx="1" transform="rotate(90)"/><rect x="-3.5" y="-16" width="7" height="32" rx="1" transform="rotate(135)"/></g><circle cx="18" cy="18" r="4.5" fill="#f0f0f0"/></svg></div>
      <h3>We have as a company</h3>
      <p>Lorem Ipsum is simply dummy text of the printing and typesetting</p>
    </div>
    <div class="feature" style="left:640px;top:133px">
      <div class="icon"><svg width="36" height="36" viewBox="0 0 36 36"><path d="M31 5L16 21l-3-3z" fill="#8e8e8e"/><path d="M12 20c-4 0-6 3-6 6 0 2-1 4-3 5 6 1 12-1 12-7z" fill="#8e8e8e"/></svg></div>
      <h3>Another prize</h3>
      <p>Lorem Ipsum is simply dummy text of the printing and typesetting</p>
    </div>
    <div class="feature" style="left:0;top:223px">
      <div class="icon"><svg width="30" height="36" viewBox="0 0 30 36"><path d="M12 12h6v7l8 14H4l8-14z" fill="#8e8e8e"/><circle cx="14" cy="3" r="2" fill="#8e8e8e"/><circle cx="18" cy="8" r="1.5" fill="#8e8e8e"/></svg></div>
      <h3>Make a subscription</h3>
      <p>Lorem Ipsum is simply dummy text of the printing and typesetting</p>
    </div>
    <div class="feature" style="left:320px;top:223px">
      <div class="icon"><svg width="30" height="36" viewBox="0 0 30 36"><rect x="9" y="2" width="18" height="26" rx="2" fill="#b5b5b5"/><path d="M4 7h17v22l-6 6H6a2 2 0 0 1-2-2z" fill="#8e8e8e"/></svg></div>
      <h3>Comparar produtos e serviços</h3>
      <p>Lorem Ipsum is simply dummy text of the printing and typesetting</p>
    </div>
    <div class="feature" style="left:640px;top:223px">
      <div class="icon"><svg width="32" height="32" viewBox="0 0 32 32"><path d="M4 17l8 8L28 8" fill="none" stroke="#8e8e8e" stroke-width="5" stroke-linecap="round" stroke-linejoin="round"/></svg></div>
      <h3>VISTORIA DE VEÍCULOSother prize</h3>
      <p>Lorem Ipsum is simply dummy text of the printing and typesetting</p>
    </div>
  </main>

  <footer class="footer">Copyright 2014.Guardiaq - All Rights Reserved</footer>
</body>
</html>
```